Brindle Barks Chews Pouch Design

I want a pouch design for my yak cheese dog chews. My competitor is golden tail, see attached. I want something minimalist like that where you see that there is only 3 ingredients, Yak milk, lime juice, Himalayan salt. I want it to say 100% natural 100% organic on it. Also odor free. There has to be a big see through window on it so you can see the products inside. Here is my logo and my competitor package. The package is 13cm x 17cm x 5cm. I have 5 sizes of bags to create but same image design

Target Market(s)

Pet owners

Industry/Entity Type

Dog products

Requirements
Must have
• « SMALL » « MIN NET WT 200 g / 5 PCS » and its important the 3 ingredients mentioned and 100% natural and organic must be very visible however the window must be big
Should not have
• The ingredients in the back

```html
<!DOCTYPE html>
<html lang="en">
<head>
<meta charset="utf-8">
<title>Brindle Barks Chews – Yak Cheese Pouch</title>
<link rel="stylesheet" href="https://fonts.googleapis.com/css2?family=Bowlby+One&family=Lilita+One&display=swap">
<style>
  :root {
    --backdrop: #e4e4e6;
    --window: #dfdfe1;
    --rose: #bf5a5a;
    --teal: #0e7d99;
    --ink: #2b1618;
    --cream: #fdf1d2;
    --gold: #f6b04a;
    --pink: #e6a39f;
    --band: #c45a5c;
  }
  * { margin: 0; padding: 0; box-sizing: border-box; }
  html, body {
    width: 1200px; height: 675px; overflow: hidden;
    background: var(--backdrop);
  }
  .canvas { position: relative; width: 1200px; height: 675px; }
  .pouch-front {
    position: absolute; left: 392px; top: 38px;
    width: 417px; height: 600px; overflow: hidden;
  }
  .pouch-shape { position: absolute; inset: 0; }
  .mascot-art {
    position: absolute; left: 114px; top: 42px;
    width: 176px; height: 176px; border-radius: 50%;
    background: radial-gradient(circle at 50% 40%, #e9963a 0%, #c36a1f 45%, #2f7f96 72%, #3d6b3a 100%);
    border: 4px solid var(--cream);
  }
  .brand-name {
    position: absolute; left: 0; right: 0; top: 228px;
    text-align: center;
    font-family: "Lilita One", sans-serif;
    font-size: 27px; line-height: 1.05;
    color: var(--ink); letter-spacing: 0.5px;
  }
  .size-tag {
    position: absolute; left: 18px; top: 96px;
    background: var(--cream); color: var(--ink);
    font-family: "Lilita One", sans-serif;
    font-size: 18px; line-height: 1; letter-spacing: 1px;
    padding: 6px 10px 5px; border-radius: 4px;
  }
  .odor-badge {
    position: absolute; left: 336px; top: 80px;
    width: 64px; height: 64px; border-radius: 50%;
    background: var(--ink);
    display: flex; flex-direction: column; align-items: center; justify-content: center;
    font-family: "Lilita One", sans-serif; color: var(--cream);
    font-size: 11px; line-height: 1.1; text-align: center;
  }
  .odor-badge::before {
    content: ""; position: absolute; inset: 3px;
    border: 1px dashed var(--cream); border-radius: 50%;
  }
  .odor-badge svg { width: 16px; height: 16px; margin-bottom: 2px; }
  .product-info {
    position: absolute; left: 0; right: 0; top: 412px;
    text-align: center;
  }
  .product-title {
    font-family: "Bowlby One", sans-serif;
    font-size: 40px; line-height: 1;
    color: var(--gold);
    -webkit-text-stroke: 2px var(--ink);
    paint-order: stroke fill;
    text-shadow: 3px 3px 0 var(--ink);
  }
  .product-subtitle {
    font-family: "Bowlby One", sans-serif;
    font-size: 27px; line-height: 1;
    color: var(--pink);
    -webkit-text-stroke: 1.5px var(--ink);
    paint-order: stroke fill;
    text-shadow: 2px 2px 0 var(--ink);
    margin-top: 3px;
  }
  .claims {
    display: flex; justify-content: center; gap: 6px; margin-top: 12px;
  }
  .claim {
    font-family: "Bowlby One", sans-serif;
    font-size: 15px; line-height: 1; padding: 4px 7px 3px;
  }
  .claim--natural { background: var(--cream); color: var(--ink); }
  .claim--organic { background: var(--ink); color: var(--cream); }
  .ingredients-label {
    font-family: "Lilita One", sans-serif;
    font-size: 15px; line-height: 1; color: var(--gold);
    margin-top: 9px; letter-spacing: 0.5px;
  }
  .ingredients-band {
    background: var(--band); color: var(--cream);
    font-family: "Lilita One", sans-serif;
    font-size: 19px; line-height: 26px;
    margin-top: 4px; letter-spacing: 0.6px;
  }
  .net-weight {
    font-family: "Lilita One", sans-serif;
    font-size: 14px; line-height: 1; color: var(--cream);
    margin-top: 7px; letter-spacing: 0.8px;
  }
</style>
</head>
<body>
<main class="canvas">
  <section class="pouch-front">
    <svg class="pouch-shape" viewBox="0 0 417 600" width="417" height="600">
      <rect x="0" y="0" width="417" height="600" fill="var(--window)"/>
      <path class="top-panel" fill="var(--rose)"
        d="M0 0 H417 V243 C410 215 400 200 380 203 C372 190 360 190 345 195
           C335 150 300 150 280 178 C250 120 120 130 118 188
           C105 178 90 180 82 200 C70 205 62 215 60 226
           C50 212 30 215 20 225 C12 222 5 225 0 230 Z"/>
      <path class="bottom-panel" fill="var(--teal)"
        d="M0 408 L30 404 L62 410 L95 402 L130 409 L170 403 L210 410 L250 404
           L290 410 L330 403 L370 409 L395 400 L417 405 V600 H0 Z"/>
    </svg>

    <div class="mascot-art" role="img" aria-label="Brand mascot illustration: happy dog with yak horns in front of mountains, sun and pine trees"></div>
    <div class="brand-name">BRINDLE BARKS<br>CHEWS</div>

    <div class="size-tag">SMALL</div>

    <div class="odor-badge">
      <svg viewBox="0 0 16 16" aria-hidden="true">
        <circle cx="8" cy="8" r="7" fill="none" stroke="var(--cream)" stroke-width="1.5"/>
        <line x1="3" y1="13" x2="13" y2="3" stroke="var(--cream)" stroke-width="1.5"/>
      </svg>
      <span>ODOR<br>FREE</span>
    </div>

    <div class="product-info">
      <h1 class="product-title">YAK CHEESE</h1>
      <h2 class="product-subtitle">DOG CHEWS</h2>
      <div class="claims">
        <span class="claim claim--natural">100% NATURAL</span>
        <span class="claim claim--organic">100% ORGANIC</span>
      </div>
      <p class="ingredients-label">ONLY 3 INGREDIENTS</p>
      <p class="ingredients-band">YAK MILK - LIME JUICE - HIMALAYAN SALT</p>
      <p class="net-weight">MIN NET WT 200 g / 5 PCS</p>
    </div>
  </section>
</main>
</body>
</html>
```